Social media app sign-up flow that asks users to give personal info and connect with other apps

Design an interactive, fun, and playful sign-up flow in which you are providing information about you, your interests, and connecting with different API plug-ins such as Fendora, WorkLoop, Tunevo, etc. (using the brand palette attached).

Basic wireframe, and business requirements are also attached.

Target Market(s)

Gen Z + Millennials (ages 22-40)

Font styles to use
Sans Serif

Colors
fbed22
fbee3d
fbf289

Requirements
Must have
• Forms for users to submit their info. Follow the color palette attached.

Connect with Fendora, Connect with WorkLoop, Connect with Tunevo, Connect with Gatherwick buttons
Nice to have
• I like the way you can use cards to submit your information for each category. Interactive card design for providing your info
Should not have
• Basic outdated designs, long forms

```html
<!DOCTYPE html>
<html lang="en">
<head>
<meta charset="utf-8">
<title>Sign-up Flow Screens</title>
<link href="https://fonts.googleapis.com/css2?family=Nunito+Sans:wght@400;600;700;800&display=swap" rel="stylesheet">
<style>
  :root {
    --canvas: #f2f3f5;
    --screen: #f8f9fb;
    --card: #f1f2f5;
    --ink: #3b3f47;
    --muted: #9aa0aa;
    --line: #c9ccd2;
    --yellow: #f8c548;
    --yellow-soft: #fbe7b3;
    --remove: #ef4b63;
    --dot: #5a6170;
  }
  * { box-sizing: border-box; margin: 0; padding: 0; }
  html, body { width: 1200px; height: 2573px; overflow: hidden; }
  body {
    background: var(--canvas);
    font-family: "Nunito Sans", sans-serif;
    color: var(--ink);
    position: relative;
  }
  .screen {
    position: absolute;
    width: 440px;
    height: 1000px;
    background: var(--screen);
    border-radius: 56px;
    box-shadow: 0 18px 40px rgba(40, 50, 70, 0.10);
    padding: 110px 40px 40px;
  }
  .screen--signup { left: 120px; top: 180px; }
  .screen--about { left: 640px; top: 180px; }
  .screen--places { left: 120px; top: 1393px; }
  .screen--music { left: 640px; top: 1393px; }

  .title { position: relative; font-size: 40px; line-height: 1.05; margin-bottom: 60px; }
  .title .light { display: block; font-weight: 400; }
  .title .bold { position: relative; display: inline-block; font-weight: 800; z-index: 1; }
  .title .bold::before {
    content: ""; position: absolute; z-index: -1;
    left: -14px; right: -40px; top: -6px; bottom: -4px;
    background: var(--yellow);
    border-radius: 4px 18px 8px 22px;
    transform: skewX(-12deg);
  }

  .field { position: relative; border: 2px solid var(--line); border-radius: 4px; height: 66px; padding: 0 24px; display: flex; align-items: center; font-size: 22px; font-weight: 600; margin-bottom: 48px; }
  .field-label { position: absolute; top: -10px; left: 20px; background: var(--screen); padding: 0 6px; font-size: 12px; color: var(--muted); }
  .continue { margin: -14px 0 80px auto; width: 136px; height: 58px; background: var(--yellow); border-radius: 4px; display: flex; align-items: center; justify-content: center; gap: 12px; font-size: 16px; font-weight: 600; box-shadow: 0 8px 18px rgba(248,197,72,.35); }

  .provider { display: flex; align-items: center; gap: 30px; height: 54px; border: 2px solid #e4e6ea; border-radius: 4px; background: #fff; padding: 0 16px; margin-bottom: 34px; font-size: 17px; font-weight: 600; box-shadow: 0 4px 10px rgba(40,50,70,.05); }
  .provider .mark { width: 32px; height: 32px; border-radius: 50%; background: var(--dot); flex: none; }
  .login-note { text-align: center; font-size: 16px; margin-top: 40px; }
  .login-note b { color: #e8a920; }

  .about-grid { display: grid; grid-template-columns: 1fr 1fr; gap: 30px 14px; }
  .topic { position: relative; height: 118px; background: var(--card); border-radius: 4px; padding: 0 24px 20px; display: flex; align-items: flex-end; font-size: 15px; font-weight: 700; line-height: 1.2; overflow: hidden; }
  .topic .art { position: absolute; right: 0; top: 0; width: 90px; height: 80px; background: linear-gradient(135deg, var(--yellow-soft), #fdf2d6); border-radius: 0 4px 0 30px; }
  .topic span { position: relative; }

  .search { height: 62px; background: var(--card); border-radius: 4px; display: flex; align-items: center; justify-content: space-between; padding: 0 24px 0 36px; font-size: 14px; font-style: italic; color: var(--muted); margin-bottom: 50px; box-shadow: 0 4px 10px rgba(40,50,70,.05); }
  .chips { display: flex; flex-wrap: wrap; gap: 32px 14px; margin-bottom: 200px; }
  .chip { position: relative; height: 62px; padding: 0 24px; background: var(--card); border-radius: 4px; display: flex; align-items: center; font-size: 15px; font-weight: 700; box-shadow: 0 4px 10px rgba(40,50,70,.05); }
  .chip .remove { position: absolute; top: -9px; right: -7px; width: 20px; height: 20px; border-radius: 50%; background: var(--remove); }
  .chip .remove::before, .chip .remove::after { content: ""; position: absolute; left: 5px; top: 9px; width: 10px; height: 2px; background: #fff; transform: rotate(45deg); }
  .chip .remove::after { transform: rotate(-45deg); }
  .connect { margin: 0 10px 40px; }
</style>
</head>
<body>

<section class="screen screen--signup">
  <h1 class="title"><span class="bold">Sign up</span></h1>
  <div class="field"><span class="field-label">Country / Region</span>United States (+1)</div>
  <div class="field"><span class="field-label">Mobile Number</span>555.204.7781</div>
  <div class="continue">Continue
    <svg width="22" height="22" viewBox="0 0 22 22"><circle cx="11" cy="11" r="9" fill="none" stroke="#3b3f47" stroke-width="2"/><path d="M7 11h8M12 8l3 3-3 3" fill="none" stroke="#3b3f47" stroke-width="2"/></svg>
  </div>
  <div class="provider"><span class="mark"></span>Sign up with Glimmer</div>
  <div class="provider"><span class="mark"></span>Sign up with Fendora</div>
  <div class="provider"><span class="mark"></span>Sign up with Orchard</div>
  <div class="provider"><span class="mark"></span>Sign up with WorkLoop</div>
  <p class="login-note">Already have an account? <b>Login</b></p>
</section>

<section class="screen screen--about">
  <h1 class="title"><span class="light">Tell me</span><span class="bold">About you</span></h1>
  <div class="about-grid">
    <div class="topic"><div class="art" role="img" aria-label="Line illustration of a house"></div><span>Places<br>I've Lived</span></div>
    <div class="topic"><div class="art" role="img" aria-label="Line illustration of a graduation cap"></div><span>Schools<br>I've Attended</span></div>
    <div class="topic"><div class="art" role="img" aria-label="Line illustration of a desk lamp"></div><span>Places<br>I've Worked</span></div>
    <div class="topic"><div class="art" role="img" aria-label="Line illustration of a handshake"></div><span>People<br>I Know</span></div>
    <div class="topic"><div class="art" role="img" aria-label="Line illustration of a party balloon"></div><span>Events<br>I've Attended</span></div>
    <div class="topic"><div class="art" role="img" aria-label="Line illustration of a drink glass"></div><span>Events<br>I'm Attending</span></div>
    <div class="topic"><div class="art" role="img" aria-label="Line illustration of headphones"></div><span>Music<br>I Love</span></div>
    <div class="topic"><div class="art" role="img" aria-label="Line illustration of a sports helmet"></div><span>Teams<br>I Love</span></div>
  </div>
</section>

<section class="screen screen--places">
  <h1 class="title"><span class="light">Places</span><span class="bold">I've Lived</span></h1>
  <div class="search">Type your location
    <svg width="22" height="22" viewBox="0 0 22 22"><circle cx="9" cy="9" r="7" fill="none" stroke="#3b3f47" stroke-width="2"/><path d="M14 14l6 6" stroke="#3b3f47" stroke-width="2"/></svg>
  </div>
  <div class="chips">
    <div class="chip">Chicago<span class="remove"></span></div>
    <div class="chip">Madrid<span class="remove"></span></div>
    <div class="chip">Paris<span class="remove"></span></div>
    <div class="chip">Rio de Janiero<span class="remove"></span></div>
    <div class="chip">Australia<span class="remove"></span></div>
  </div>
  <div class="provider connect"><span class="mark"></span>Connect with Fendora</div>
  <div class="provider connect"><span class="mark"></span>Connect with WorkLoop</div>
</section>

<section class="screen screen--music">
  <h1 class="title"><span class="light">Music</span><span class="bold">I Love</span></h1>
  <div class="search">Type your band or musician
    <svg width="22" height="22" viewBox="0 0 22 22"><circle cx="9" cy="9" r="7" fill="none" stroke="#3b3f47" stroke-width="2"/><path d="M14 14l6 6" stroke="#3b3f47" stroke-width="2"/></svg>
  </div>
  <div class="chips">
    <div class="chip">The Lanterns<span class="remove"></span></div>
    <div class="chip">Marisol<span class="remove"></span></div>
    <div class="chip">Forty Bars<span class="remove"></span></div>
    <div class="chip">Ray Calder<span class="remove"></span></div>
    <div class="chip">Brinley Shore<span class="remove"></span></div>
  </div>
  <div class="provider connect"><span class="mark"></span>Connect with Fendora</div>
  <div class="provider connect"><span class="mark"></span>Connect with Tunevo</div>
</section>

</body>
</html>
```